Orvane Business Hub Website Redesign

Objective: The primary goal of the website redesign is to effectively communicate with Small Business Owners, offering them custom business advisory services to drive growth. The redesigned website should be interactive, easy to read, and feature clear calls to action.

OBH provides custom business advisory services tailored to small enterprises, focusing on driving growth through a comprehensive 3-step process; Diagnostic, Remedial and Strategic roadmap development

1. Diagnostic Assessment:
a. In-depth analysis to identify business strengths, weaknesses, and opportunities.
b. Comprehensive evaluation to understand the unique needs of each small enterprise.
2. Remedial Care:
a. Implementation of tailored solutions to address identified issues.
b. Hands-on support to navigate challenges and obstacles.
3. Roadmap to Growth:
a. Development of a strategic roadmap outlining actionable steps for sustainable growth.
b. Ongoing guidance and support to ensure successful execution.

The Unique Selling Proposition (USP): OBH stands out by:
• Handholding businesses through their growth journey.
• Providing a clear roadmap to sustainable growth.
• Leveraging a network of industry experts for specialized advice.
Target Customers: OBH caters to the following target customers:
• Start-ups seeking to launch successfully.
• Businesses looking to achieve substantial growth.
• Entrepreneurial enterprises seeking support.
• Mature businesses facing distress and seeking turnaround strategies.
Services Offered:
1. Bespoke Packages:
a. Tailored advisory services to meet the unique needs of each client.
b. Personalized solutions for businesses at different stages of growth.
2. Training, Mentorship, and Coaching:
a. Skill-building programs for business owners and key staff.
b. Ongoing mentorship and coaching to foster continuous improvement.
3. Incubation:
a. Support for start-ups with physical and virtual resources.
b. Incubation programs to nurture and guide emerging businesses.
4. Specialized Programs:
a. Women Entrepreneurs:
b. Tailored programs to support and empower women in business.
c. Youth Entrepreneurs: Initiatives to cultivate and guide young entrepreneurs.

Design Preferences:
• Layout flow to tell the brand story
• Interactive design elements
• Easy-to-read and understand content.
• Clear and prominent calls to action.
Key Messages:
• Expert Business Advisory for Small Enterprises.
• Your Partner in Growth – from Assessment to Execution.
• Join a Network of Successful Entrepreneurs.
Brand Guidelines:
• Use the existing brand colors and logo.
• Maintain a professional and approachable tone throughout the website.
Deliverables:
• Responsive website design for desktop and mobile.
• Mockups for key pages.
• Clear navigation structure for easy user experience.
• Integration of interactive elements.

Similar Businesses
https://trellowventures.co.uk/free-resources/
https://www.kestrinvale.ac.uk/business-services/engage-with-us/talent-and-insight/the-venture-desk/
https://www.foundermill.ng/the-venture-desk/
https://plumewardadvisory.io/

Design ad Layout Inspiration
https://volubrique.com/en/
https://www.qz-example.com/en_gl/big-data-analytics

Target Market(s)

OBH caters to the following target customers: • Start-ups seeking to launch successfully. • Businesses looking to achieve substantial growth. • Entrepreneurial enterprises seeking support. • Mature businesses facing distress and seeking turnaround strategies.

Industry/Entity Type

Business Consulting and Advisory

Number of Pages Required

3 page

Requirements
Must have
• • Clear and prominent calls to action.
Nice to have
• • Interactive design elements. • Easy-to-read and understand content.

```html
<!DOCTYPE html>
<html lang="en">
<head>
<meta charset="utf-8">
<title>Orvane Business Hub — Expert Advisory Services</title>
<link href="https://fonts.googleapis.com/css2?family=Montserrat:wght@400;500;600;700&display=swap" rel="stylesheet">
<style>
:root{
  --teal:#137a82;
  --teal-deep:#0b5a61;
  --cyan:#23b4e8;
  --navy:#0d2a42;
  --ink:#111;
  --muted:#555;
  --soft:#eef5f7;
  --aqua:#7fd2d6;
  --white:#fff;
  --black:#000;
}
*{margin:0;padding:0;box-sizing:border-box}
html,body{width:1200px;height:4227px;overflow:hidden}
body{font-family:'Montserrat',sans-serif;color:var(--ink);background:var(--white);position:relative}
section,header,footer{position:absolute;left:0;width:1200px}
.abs{position:absolute}
.eyebrow{color:var(--cyan);font-size:16px;font-weight:400}
.h2{font-size:36px;font-weight:500;line-height:1.15;color:var(--ink)}
.btn{position:absolute;display:flex;align-items:center;justify-content:center;background:var(--cyan);color:var(--navy);font-size:14px;font-weight:600;border-radius:2px}
.ph{position:absolute}

/* header */
.site-header{top:0;height:89px;background:var(--white)}
.brand{position:absolute;left:97px;top:30px;font-size:19px;font-weight:700;color:var(--navy);display:flex;align-items:center;gap:8px}
.brand-dot{width:12px;height:12px;background:var(--cyan);flex:none}
.nav{position:absolute;top:38px;left:448px;font-size:13px}
.nav span{position:absolute;white-space:nowrap}
.contact-mini{position:absolute;left:985px;top:27px;font-size:11px;color:var(--muted)}
.contact-mini strong{display:block;font-size:15px;font-weight:500;color:var(--ink);margin-top:4px}

/* hero */
.hero{top:89px;height:448px;background:linear-gradient(100deg,#0e6f77 0%,#1b8b92 55%,#2a9ea3 100%)}
.hero-text{position:absolute;left:97px;top:138px;color:var(--white)}
.hero-text .l1{font-size:29px;font-weight:400}
.hero-text .l2{font-size:40px;font-weight:700;line-height:1.3;margin-top:6px}
.hero-text .l2 em{font-weight:400;font-size:29px}

/* welcome */
.welcome{top:537px;height:576px}
.welcome p{position:absolute;left:601px;top:281px;width:394px;font-size:13px;line-height:21.2px;color:var(--muted)}

/* how */
.how{top:1113px;height:757px;background:linear-gradient(135deg,#f4f8f9,#e9f2f4 60%,#f3f7f8)}
.center{position:absolute;left:0;width:1200px;text-align:center}
.step-num{position:absolute;width:79px;height:79px;border-radius:50%;background:#dfe9ed;display:flex;align-items:center;justify-content:center}
.step-num span{width:62px;height:62px;border-radius:50%;background:var(--navy);border:4px solid var(--cyan);color:var(--white);font-size:24px;font-weight:600;display:flex;align-items:center;justify-content:center}
.step-title{position:absolute;font-size:17px;font-weight:600;white-space:nowrap}
.step-pt{position:absolute;width:300px;font-size:11.5px;line-height:18px;color:var(--muted)}
.step-pt.left{text-align:right;padding-right:24px}
.step-pt.right{padding-left:24px}
.step-pt svg{position:absolute;top:1px}
.step-pt.left svg{right:0}
.step-pt.right svg{left:0}

/* usp */
.usp{top:1870px;height:528px;background:var(--black);color:var(--white)}
.usp h2{position:absolute;left:151px;top:124px;font-size:36px;font-weight:500;line-height:44px}
.usp h2 span{color:var(--cyan)}
.usp ul{position:absolute;left:151px;top:272px;list-style:none;font-size:15px;width:460px}
.usp li{position:relative;padding-left:28px;line-height:22px;margin-bottom:18px}
.usp li svg{position:absolute;left:0;top:4px}

/* services */
.services{top:2398px;height:762px}
.card{position:absolute;top:217px;width:212px;height:389px;border:1px solid #d9dde0;border-radius:4px;background:var(--white);box-shadow:0 1px 4px rgba(0,0,0,.06)}
.card .ph{left:5px;top:5px;width:200px;height:148px}
.card h3{position:absolute;left:20px;top:170px;width:180px;font-size:15px;font-weight:600;line-height:20px}
.card .pts{position:absolute;left:20px;top:220px;width:180px}
.card .pt{position:relative;padding-left:26px;font-size:11.5px;line-height:18px;color:var(--muted);margin-bottom:14px}
.card .pt svg{position:absolute;left:0;top:2px}
.card .sub{font-size:12px;font-weight:600;color:#333;margin-bottom:6px}
.card .pts.tight .pt{margin-bottom:10px}

/* connect */
.connect{top:3160px;height:558px;background:linear-gradient(135deg,#86d8da,#72cbd0 60%,#8ad9dc)}
.connect h2{position:absolute;left:146px;top:78px;font-size:36px;font-weight:500;line-height:42px}
.connect .lead{position:absolute;left:146px;top:172px;width:420px;font-size:15px;line-height:24px}
.field{position:absolute;left:701px;width:350px;height:43px;background:var(--white);border:1px solid #cfd8da;font-size:13px;padding:14px;color:#222}
.connect .check{position:absolute;left:701px;top:325px;width:14px;height:14px;border:1px solid #555;background:var(--white)}
.connect .consent-text{position:absolute;left:728px;top:323px;width:320px;font-size:11.5px;line-height:16px;color:#2a4a50}
.submit{position:absolute;left:701px;top:394px;width:350px;height:44px;background:var(--black);color:var(--cyan);font-size:14px;font-weight:600;display:flex;align-items:center;justify-content:center}

/* partners */
.partners{top:3718px;height:118px;background:var(--white)}
.badge{position:absolute;top:42px;width:70px;height:36px;background:#c9cdd0;border-radius:4px}

/* footer */
.site-footer{top:3836px;height:391px;background:var(--black);color:var(--white)}
.vline{position:absolute;top:0;width:1px;height:308px;background:#2c2c2c}
.f-brand{position:absolute;left:148px;top:86px;font-size:20px;font-weight:700;line-height:24px;display:flex;align-items:center;gap:8px}
.social{position:absolute;top:174px;width:33px;height:33px;border:1.5px solid var(--white);border-radius:50%}
.f-head{position:absolute;top:48px;font-size:16px;font-weight:500;letter-spacing:.5px}
.f-links{position:absolute;left:405px;top:94px;font-size:13px;color:#bbb}
.f-links div{height:32.4px}
.ci{position:absolute;left:614px;font-size:13px}
.ci b{display:block;font-weight:600;color:var(--white)}
.ci span{display:block;color:#bbb;line-height:20px;margin-top:4px}
.ci svg{position:absolute;left:-24px;top:1px}
.nl-text{position:absolute;left:842px;top:93px;font-size:13px;color:#ccc}
.nl-field{position:absolute;left:842px;top:124px;width:209px;height:34px;background:var(--white);color:#222;font-size:13px;padding:10px 14px}
.nl-send{position:absolute;right:3px;top:3px;width:28px;height:28px;background:var(--cyan);display:flex;align-items:center;justify-content:center}
.hline{position:absolute;left:145px;top:316px;width:910px;height:1px;background:#2c2c2c}
.copy{position:absolute;left:145px;top:348px;font-size:12.5px;color:#aaa}
.legal{position:absolute;left:827px;top:348px;font-size:12.5px;font-weight:600;white-space:nowrap}
</style>
</head>
<body>

<header class="site-header">
  <div class="brand"><span class="brand-dot"></span>Orvane Business Hub</div>
  <nav class="nav">
    <span style="left:0">About Us</span>
    <span style="left:90px">Services</span>
    <span style="left:174px">Testimonials</span>
    <span style="left:286px">Contact Us</span>
  </nav>
  <div class="contact-mini">
    <svg width="14" height="14" viewBox="0 0 14 14" style="vertical-align:-3px;margin-right:4px"><rect width="14" height="14" rx="2" fill="#23b4e8"/><path d="M4 3.5l1.5-.5 1 2-1 .8a5 5 0 0 0 2.7 2.7l.8-1 2 1-.5 1.5C7 10.5 3.5 7 4 3.5z" fill="#fff"/></svg>Any Questions?
    <strong>555-014-2290</strong>
  </div>
</header>

<section class="hero">
  <div class="ph" role="img" aria-label="Photo of an advisory team meeting around a conference table, tinted teal" style="inset:0;background:linear-gradient(100deg,rgba(10,90,97,.95) 0%,rgba(24,130,137,.7) 45%,rgba(60,160,165,.55) 100%)"></div>
  <div class="hero-text">
    <div class="l1">Unlock Your Business Potential</div>
    <div class="l2"><em>with</em> EXPERT ADVISORY<br>SERVICES</div>
  </div>
  <div class="btn" style="left:97px;top:320px;width:153px;height:44px">Get In Touch</div>
</section>

<section class="welcome">
  <div class="ph" role="img" aria-label="Photo of two business professionals reviewing a tablet together" style="left:161px;top:83px;width:343px;height:421px;background:linear-gradient(160deg,#c9c6c0,#8c7e70 50%,#3c3b3e)"></div>
  <div class="abs eyebrow" style="left:601px;top:130px">Welcome to OBH</div>
  <h2 class="abs h2" style="left:601px;top:157px">Your Partner in<br>Growth!</h2>
  <svg class="abs" style="left:601px;top:248px" width="118" height="12" viewBox="0 0 118 12"><path d="M0 6h14l3-5 3 10 3-5h95" fill="none" stroke="#333" stroke-width="1"/></svg>
  <p>At OBH, we understand the unique challenges and opportunities that small enterprises face. Our mission is to provide customized business advisory services to drive growth, supporting businesses at every stage of their journey. Whether you're a startup aiming for a successful launch, a business striving for substantial growth, an entrepreneurial enterprise in need of support, or a mature business facing distress, OBH is here for you.</p>
</section>

<section class="how">
  <div class="center eyebrow" style="top:60px">Three-step process</div>
  <h2 class="center h2" style="top:86px">How it Works</h2>
  <svg class="abs" style="left:518px;top:135px" width="164" height="12" viewBox="0 0 164 12"><path d="M0 6h76l3-5 3 10 3-5h79" fill="none" stroke="#333" stroke-width="1"/></svg>

  <svg class="abs" style="left:0;top:0" width="1200" height="757">
    <g fill="none" stroke="#b9c4c8" stroke-width="1" stroke-dasharray="3 3">
      <path d="M519 228V710M519 228h41M486 410h33M519 527h41M680 378v150h35M640 378h40M519 710h-33"/>
      <path d="M599 266v110M599 417v110" stroke-dasharray="2 8" stroke-width="3" stroke-linecap="round"/>
    </g>
  </svg>
  <div class="step-num" style="left:560px;top:188px"><span>01</span></div>
  <div class="step-num" style="left:560px;top:339px"><span>02</span></div>
  <div class="step-num" style="left:560px;top:488px"><span>03</span></div>

  <svg class="abs" style="left:443px;top:206px" width="42" height="42" viewBox="0 0 42 42" fill="none" stroke="#0d2a42" stroke-width="1.4"><rect x="4" y="6" width="26" height="32" rx="2"/><path d="M9 14h16M9 20h16M9 26h10"/><path d="M26 30l10-16 3 2-10 16-4 1z" stroke="#23b4e8"/></svg>
  <div class="step-title" style="right:716px;top:258px">Diagnostic Assessment</div>
  <div class="step-pt left" style="left:186px;top:293px">In-depth analysis to identify business strengths, weaknesses, and opportunities.<svg width="15" height="15" viewBox="0 0 15 15"><circle cx="7.5" cy="7.5" r="6.5" fill="none" stroke="#333"/><path d="M4.5 7.5l2 2 4-4" fill="none" stroke="#333"/></svg></div>
  <div class="step-pt left" style="left:186px;top:342px">Comprehensive evaluation to understand the unique needs of each small enterprise.<svg width="15" height="15" viewBox="0 0 15 15"><circle cx="7.5" cy="7.5" r="6.5" fill="none" stroke="#333"/><path d="M4.5 7.5l2 2 4-4" fill="none" stroke="#333"/></svg></div>

  <svg class="abs" style="left:712px;top:346px" width="56" height="50" viewBox="0 0 56 50" fill="none" stroke="#0d2a42" stroke-width="1.4"><circle cx="16" cy="16" r="13"/><path d="M16 10v12M10 16h12" stroke="#23b4e8"/><rect x="24" y="22" width="28" height="22" rx="11"/><path d="M32 31h12M32 36h8"/></svg>
  <div class="step-title" style="left:714px;top:408px">Remedial Care</div>
  <div class="step-pt right" style="left:714px;top:450px">Implementation of tailored solutions to address identified issues.<svg width="15" height="15" viewBox="0 0 15 15"><circle cx="7.5" cy="7.5" r="6.5" fill="none" stroke="#333"/><path d="M4.5 7.5l2 2 4-4" fill="none" stroke="#333"/></svg></div>
  <div class="step-pt right" style="left:714px;top:499px">Hands-on support to navigate challenges and obstacles.<svg width="15" height="15" viewBox="0 0 15 15"><circle cx="7.5" cy="7.5" r="6.5" fill="none" stroke="#333"/><path d="M4.5 7.5l2 2 4-4" fill="none" stroke="#333"/></svg></div>

  <svg class="abs" style="left:440px;top:508px" width="46" height="48" viewBox="0 0 46 48" fill="none" stroke="#0d2a42" stroke-width="1.4"><rect x="10" y="4" width="30" height="34" rx="2"/><path d="M16 30V22M22 30V16M28 30V19M34 30V12" stroke="#23b4e8"/><circle cx="10" cy="38" r="7"/><circle cx="10" cy="38" r="2.5"/></svg>
  <div class="step-title" style="right:713px;top:563px">Roadmap to Growth</div>
  <div class="step-pt left" style="left:186px;top:604px">Development of a strategic roadmap outlining actionable steps for sustainable growth.<svg width="15" height="15" viewBox="0 0 15 15"><circle cx="7.5" cy="7.5" r="6.5" fill="none" stroke="#333"/><path d="M4.5 7.5l2 2 4-4" fill="none" stroke="#333"/></svg></div>
  <div class="step-pt left" style="left:186px;top:653px">Ongoing guidance and support to ensure successful execution.<svg width="15" height="15" viewBox="0 0 15 15"><circle cx="7.5" cy="7.5" r="6.5" fill="none" stroke="#333"/><path d="M4.5 7.5l2 2 4-4" fill="none" stroke="#333"/></svg></div>
</section>

<section class="usp">
  <h2>The Unique Selling<br>Proposition <span>(USP)</span></h2>
  <svg class="abs" style="left:151px;top:234px" width="118" height="12" viewBox="0 0 118 12"><path d="M0 6h14l3-5 3 10 3-5h95" fill="none" stroke="#fff" stroke-width="1"/></svg>
  <ul>
    <li><svg width="14" height="14" viewBox="0 0 15 15"><circle cx="7.5" cy="7.5" r="6.5" fill="none" stroke="#23b4e8" stroke-width="1.4"/><path d="M4.5 7.5l2 2 4-4" fill="none" stroke="#23b4e8" stroke-width="1.4"/></svg>Handholding businesses through their growth journey.</li>
    <li><svg width="14" height="14" viewBox="0 0 15 15"><circle cx="7.5" cy="7.5" r="6.5" fill="none" stroke="#23b4e8" stroke-width="1.4"/><path d="M4.5 7.5l2 2 4-4" fill="none" stroke="#23b4e8" stroke-width="1.4"/></svg>Businesses looking to achieve substantial growth.</li>
    <li><svg width="14" height="14" viewBox="0 0 15 15"><circle cx="7.5" cy="7.5" r="6.5" fill="none" stroke="#23b4e8" stroke-width="1.4"/><path d="M4.5 7.5l2 2 4-4" fill="none" stroke="#23b4e8" stroke-width="1.4"/></svg>Entrepreneurial enterprises seeking support.</li>
    <li><svg width="14" height="14" viewBox="0 0 15 15"><circle cx="7.5" cy="7.5" r="6.5" fill="none" stroke="#23b4e8" stroke-width="1.4"/><path d="M4.5 7.5l2 2 4-4" fill="none" stroke="#23b4e8" stroke-width="1.4"/></svg>Mature businesses facing distress and seeking turnaround strategies.</li>
  </ul>
  <div class="ph" role="img" aria-label="Photo of two smiling colleagues looking at a tablet" style="left:616px;top:34px;width:500px;height:494px;background:radial-gradient(ellipse at 55% 60%,#3a3f4a 0%,#1c1f26 55%,#000 80%)"></div>
  <svg class="abs" style="left:812px;top:239px" width="96" height="96" viewBox="0 0 96 96"><circle cx="48" cy="48" r="46" fill="none" stroke="#fff" stroke-width="1.5" stroke-dasharray="2 6"/><path d="M40 33l22 15-22 15z" fill="#23b4e8"/></svg>
</section>

<section class="services">
  <div class="center eyebrow" style="top:86px">Services Offered</div>
  <h2 class="center h2" style="top:116px">Services We Offer</h2>
  <svg class="abs" style="left:518px;top:167px" width="164" height="12" viewBox="0 0 164 12"><path d="M0 6h76l3-5 3 10 3-5h79" fill="none" stroke="#333" stroke-width="1"/></svg>

  <div class="card" style="left:151px">
    <div class="ph" role="img" aria-label="Photo of a consulting meeting at a table" style="background:linear-gradient(150deg,#b9c2c6,#5d666c)"></div>
    <h3 style="top:180px">Bespoke Packages</h3>
    <div class="pts">
      <div class="pt"><svg width="13" height="13" viewBox="0 0 15 15"><circle cx="7.5" cy="7.5" r="6.5" fill="none" stroke="#23b4e8"/><path d="M4.5 7.5l2 2 4-4" fill="none" stroke="#23b4e8"/></svg>Tailored advisory services to meet the unique needs of each client.</div>
      <div class="pt"><svg width="13" height="13" viewBox="0 0 15 15"><circle cx="7.5" cy="7.5" r="6.5" fill="none" stroke="#23b4e8"/><path d="M4.5 7.5l2 2 4-4" fill="none" stroke="#23b4e8"/></svg>Personalized solutions for businesses at different stages of growth.</div>
    </div>
  </div>
  <div class="card" style="left:381px">
    <div class="ph" role="img" aria-label="Photo of a trainer presenting at a whiteboard to a group" style="background:linear-gradient(150deg,#d6dadc,#7c858a)"></div>
    <h3>Training, Mentorship, and Coaching</h3>
    <div class="pts">
      <div class="pt"><svg width="13" height="13" viewBox="0 0 15 15"><circle cx="7.5" cy="7.5" r="6.5" fill="none" stroke="#23b4e8"/><path d="M4.5 7.5l2 2 4-4" fill="none" stroke="#23b4e8"/></svg>Skill-building programs for business owners and key staff.</div>
      <div class="pt"><svg width="13" height="13" viewBox="0 0 15 15"><circle cx="7.5" cy="7.5" r="6.5" fill="none" stroke="#23b4e8"/><path d="M4.5 7.5l2 2 4-4" fill="none" stroke="#23b4e8"/></svg>Ongoing mentorship and coaching to foster continuous improvement.</div>
    </div>
  </div>
  <div class="card" style="left:611px">
    <div class="ph" role="img" aria-label="Photo of a start-up team working in a bright studio" style="background:linear-gradient(150deg,#e3e8eb,#8fa4b0)"></div>
    <h3 style="top:180px">Incubation</h3>
    <div class="pts">
      <div class="pt"><svg width="13" height="13" viewBox="0 0 15 15"><circle cx="7.5" cy="7.5" r="6.5" fill="none" stroke="#23b4e8"/><path d="M4.5 7.5l2 2 4-4" fill="none" stroke="#23b4e8"/></svg>Support for start-ups with physical and virtual resources.</div>
      <div class="pt"><svg width="13" height="13" viewBox="0 0 15 15"><circle cx="7.5" cy="7.5" r="6.5" fill="none" stroke="#23b4e8"/><path d="M4.5 7.5l2 2 4-4" fill="none" stroke="#23b4e8"/></svg>Incubation programs to nurture and guide emerging businesses.</div>
    </div>
  </div>
  <div class="card" style="left:839px">
    <div class="ph" role="img" aria-label="Photo of young professionals at a workshop board" style="background:linear-gradient(150deg,#b7a99e,#5f5753)"></div>
    <h3 style="top:180px">Specialized Programs</h3>
    <div class="pts tight" style="top:208px">
      <div class="sub">Women Entrepreneurs:</div>
      <div class="pt"><svg width="13" height="13" viewBox="0 0 15 15"><circle cx="7.5" cy="7.5" r="6.5" fill="none" stroke="#23b4e8"/><path d="M4.5 7.5l2 2 4-4" fill="none" stroke="#23b4e8"/></svg>Tailored programs to support and empower women in business.</div>
      <div class="sub">Youth Entrepreneurs:</div>
      <div class="pt"><svg width="13" height="13" viewBox="0 0 15 15"><circle cx="7.5" cy="7.5" r="6.5" fill="none" stroke="#23b4e8"/><path d="M4.5 7.5l2 2 4-4" fill="none" stroke="#23b4e8"/></svg>Initiatives to cultivate and guide young entrepreneurs.</div>
    </div>
  </div>
  <div class="btn" style="left:524px;top:644px;width:153px;height:44px">Get In Touch</div>
</section>

<section class="connect">
  <h2>Let's Connect And<br>Grow Together</h2>
  <div class="lead">Reach Out to Us for Expert Guidance and Support on Your Business Journey</div>
  <div class="ph" role="img" aria-label="Overhead photo of three people collaborating around a laptop at a round table" style="left:159px;top:222px;width:399px;height:336px;background:radial-gradient(ellipse at 50% 55%,#3d4f6a 0%,#55657a 40%,rgba(120,205,210,0) 72%)"></div>
  <div class="field" style="top:135px">First Name</div>
  <div class="field" style="top:195px">Email</div>
  <div class="field" style="top:256px">Phone No</div>
  <div class="check"></div>
  <div class="consent-text">I agree to receive updates from OBH and allow my details to be stored securely and used only to reply to my enquiry.</div>
  <div class="submit">Submit</div>
</section>

<section class="partners">
  <div class="badge" style="left:146px;border-radius:50%;width:72px"></div>
  <div class="badge" style="left:315px"></div>
  <div class="badge" style="left:484px"></div>
  <div class="badge" style="left:651px"></div>
  <div class="badge" style="left:822px;width:54px;height:48px;top:36px"></div>
  <div class="badge" style="left:976px"></div>
</section>

<footer class="site-footer">
  <div class="vline" style="left:363px"></div>
  <div class="vline" style="left:808px"></div>
  <div class="f-brand"><span class="brand-dot"></span>Orvane<br>Business Hub</div>
  <div class="social" style="left:158px"></div>
  <div class="social" style="left:204px"></div>
  <div class="social" style="left:248px"></div>

  <div class="f-head" style="left:405px">QUICK LINKS</div>
  <div class="f-links">
    <div>About Us</div><div>Services</div><div>Training</div><div>Products</div><div>Consultancy</div><div>Contact Us</div>
  </div>

  <div class="f-head" style="left:588px">CONTACT INFO</div>
  <div class="ci" style="top:96px"><svg width="12" height="14" viewBox="0 0 12 14"><path d="M6 13S1 8 1 5a5 5 0 0 1 10 0c0 3-5 8-5 8z" fill="#23b4e8"/><circle cx="6" cy="5" r="1.8" fill="#000"/></svg><b>Address:</b><span>48 Harrowgate Lane<br>Brookmere, CA 90210</span></div>
  <div class="ci" style="top:173px"><svg width="13" height="13" viewBox="0 0 14 14"><path d="M2 1.5l3-.5 1.5 3-1.5 1.2a7 7 0 0 0 3.8 3.8l1.2-1.5 3 1.5-.5 3C6 13 1 8 2 1.5z" fill="#23b4e8"/></svg><b>Phone:</b><span>555-014-2290</span></div>
  <div class="ci" style="top:231px"><svg width="14" height="11" viewBox="0 0 14 11"><rect width="14" height="11" rx="1" fill="#23b4e8"/><path d="M1 1l6 5 6-5" fill="none" stroke="#000" stroke-width="1.2"/></svg><b>Email:</b><span>hello@orvanehub.example</span></div>

  <div class="f-head" style="left:842px">OUR NEWSLETTER</div>
  <div class="nl-text">Sign Up to get latest updates!</div>
  <div class="nl-field">Email Address<span class="nl-send"><svg width="14" height="14" viewBox="0 0 14 14"><path d="M1 6.5L13 1 9 13 6.5 8z" fill="#fff"/></svg></span></div>

  <div class="hline"></div>
  <div class="copy">© 2024 All Rights Reserved | OBH</div>
  <div class="legal">Privacy Policy &nbsp;&nbsp;&nbsp;|&nbsp;&nbsp;&nbsp; Terns &amp; Conditions</div>
</footer>

</body>
</html>
```